Stationery Design Project

We need a stationery design for a new business consulting business based in New Zealand.
We have the logo and business cards designed and we're looking for letterhead, compliments slip and slide deck presentation format that aligns with our business cards.
Industry/Entity Type
Business
Requirements
Must have
- same colors and format as business cards

```html
<!DOCTYPE html>
<html lang="en">
<head>
<meta charset="utf-8">
<title>Halden Consulting Stationery</title>
<link rel="stylesheet" href="https://fonts.googleapis.com/css2?family=Arimo:wght@400;700&family=Pinyon+Script&display=swap">
<style>
  :root {
    --backdrop: #5d6667;
    --lime: #8cff0a;
    --slate: #98a6a5;
    --brand-grey: #8e9c9c;
    --ink: #111;
    --meta: #8a9696;
    --paper: #ffffff;
    --plant-tone: #a6ff45;
  }
  * { box-sizing: border-box; margin: 0; padding: 0; }
  html, body { width: 1200px; height: 1200px; overflow: hidden; }
  body { background: var(--backdrop); font-family: "Arimo", Arial, sans-serif; position: relative; }

  .sheet { position: absolute; background: var(--paper); box-shadow: 2px 3px 8px rgba(0,0,0,.35); overflow: hidden; }
  .band { position: absolute; background: var(--lime); }
  .bar { position: absolute; background: var(--slate); }

  .wordmark { position: absolute; display: flex; align-items: center; gap: 6px; color: var(--brand-grey); font-weight: 400; letter-spacing: -.5px; white-space: nowrap; }
  .wordmark .dot { width: .32em; height: .32em; border-radius: 50%; background: var(--brand-grey); }

  .contact { position: absolute; color: var(--meta); font-weight: 700; line-height: 1.4; white-space: nowrap; }
  .contact .row { display: flex; align-items: center; gap: 4px; }
  .contact svg { width: 1em; height: 1em; flex: none; }

  /* Letterhead */
  .letterhead { left: 42px; top: 52px; width: 765px; height: 1080px; }
  .letterhead .band { left: 330px; top: 0; width: 435px; height: 68px; }
  .letterhead .bar { left: 0; top: 855px; width: 55px; height: 225px; }
  .letterhead .wordmark { left: 68px; top: 76px; font-size: 30px; }
  .letterhead .contact { left: 330px; top: 78px; font-size: 10.5px; }
  .letter { position: absolute; left: 90px; top: 280px; width: 600px; font-size: 15.5px; line-height: 22px; color: var(--ink); }
  .letter p { margin-bottom: 22px; }
  .letter .date { margin-bottom: 36px; }

  /* Business card */
  .card { left: 757px; top: 288px; width: 343px; height: 204px; background: linear-gradient(100deg, #c9cdcd 0%, #eceeee 45%, #ffffff 100%); }
  .card .band { left: 153px; top: 0; width: 190px; height: 22px; }
  .card .bar { left: 4px; top: 105px; width: 20px; height: 99px; }
  .card .wordmark { left: 24px; top: 52px; font-size: 29px; gap: 4px; }
  .card .holder { position: absolute; left: 92px; top: 131px; text-align: right; }
  .card .holder .name { color: var(--lime); font-size: 11px; font-weight: 700; }
  .card .holder .role { color: var(--meta); font-size: 7px; }
  .card .contact { left: 208px; top: 128px; font-size: 7px; }

  /* Compliments slip */
  .slip-back { left: 412px; top: 735px; width: 766px; height: 360px; background: var(--lime); }
  .slip-back .plant { position: absolute; left: 436px; top: 247px; width: 240px; height: 113px; background: linear-gradient(180deg, var(--lime), var(--plant-tone)); }
  .slip { left: 334px; top: 632px; width: 766px; height: 361px; }
  .slip .band { left: 416px; top: 0; width: 350px; height: 43px; }
  .slip .bar { left: 0; top: 183px; width: 44px; height: 178px; }
  .slip .wordmark { left: 144px; top: 48px; font-size: 30px; }
  .slip .contact { left: 416px; top: 56px; font-size: 10.5px; }
  .slip .greeting { position: absolute; left: 414px; top: 186px; font-family: "Pinyon Script", cursive; font-size: 44px; color: var(--lime); white-space: nowrap; }
</style>
</head>
<body>

<section class="sheet letterhead">
  <div class="band"></div>
  <div class="wordmark"><span class="dot"></span>HaldenConsulting</div>
  <div class="contact">
    <div class="row">PO Box 41820</div>
    <div class="row">Wellington 6140 New Zealand</div>
    <div class="row"><svg viewBox="0 0 10 10"><path d="M2 1 L4 1 L4.6 3 L3.5 3.8 Q4.5 5.8 6.2 6.5 L7 5.4 L9 6 L9 8 Q5 9 2.2 5.5 Q1 3.5 2 1Z" fill="#8cff0a"/></svg>+ 64 21 555 0142</div>
    <div class="row"><svg viewBox="0 0 10 10"><rect x="1" y="2.5" width="8" height="5.5" fill="none" stroke="#8cff0a"/><path d="M1 2.5 L5 5.6 L9 2.5" fill="none" stroke="#8cff0a"/></svg>hello@haldenconsulting.com</div>
    <div class="row"><svg viewBox="0 0 10 10"><circle cx="5" cy="5" r="4" fill="none" stroke="#8cff0a"/><path d="M1 5 H9 M5 1 Q2.5 5 5 9 M5 1 Q7.5 5 5 9" fill="none" stroke="#8cff0a"/></svg>www.haldenconsulting.com</div>
  </div>
  <article class="letter">
    <p class="date">Oktober 13, 2011</p>
    <p>Mr. Owen Hartley<br>PO Box 30517<br>Wellington 6011 New Zealand</p>
    <p>Dear Mr. Hartley,</p>
    <p>typically, the client has second language issues, for instance born and raised<br>in Asia, Latin America, Europe , or elsewhere OR perhaps a native-born citizen<br>who is in need of English skills building.</p>
    <p>In the workplace, the professional requires high-skill competency<br>&nbsp;for intra/interdepartmental networking, conference calling, slide deck<br>presentations, management reports, client meetings, staff briefings<br>and evaluations, etc. Lacking these skills can hold back career<br>performance and personal confidence.</p>
    <p>With deepest sympathy,</p>
    <p>Executive Director</p>
  </article>
  <div class="bar"></div>
</section>

<section class="sheet card">
  <div class="band"></div>
  <div class="wordmark"><span class="dot"></span>HaldenConsulting</div>
  <div class="bar"></div>
  <div class="holder">
    <div class="name">CONSULTANT NAME</div>
    <div class="role">Senior Consultant</div>
  </div>
  <div class="contact">
    <div class="row">PO Box 41820</div>
    <div class="row">Wellington 6140 New Zealand</div>
    <div class="row">+ 64 21 555 0142</div>
    <div class="row">hello@haldenconsulting.com</div>
    <div class="row">www.haldenconsulting.com</div>
  </div>
</section>

<section class="sheet slip-back">
  <div class="plant" role="img" aria-label="Decorative white line drawing of grass and flower stems"></div>
</section>

<section class="sheet slip">
  <div class="band"></div>
  <div class="wordmark"><span class="dot"></span>HaldenConsulting</div>
  <div class="contact">
    <div class="row">PO Box 41820</div>
    <div class="row">Wellington 6140 New Zealand</div>
    <div class="row"><svg viewBox="0 0 10 10"><path d="M2 1 L4 1 L4.6 3 L3.5 3.8 Q4.5 5.8 6.2 6.5 L7 5.4 L9 6 L9 8 Q5 9 2.2 5.5 Q1 3.5 2 1Z" fill="#8cff0a"/></svg>+ 64 21 555 0142</div>
    <div class="row"><svg viewBox="0 0 10 10"><rect x="1" y="2.5" width="8" height="5.5" fill="none" stroke="#8cff0a"/><path d="M1 2.5 L5 5.6 L9 2.5" fill="none" stroke="#8cff0a"/></svg>hello@haldenconsulting.com</div>
    <div class="row"><svg viewBox="0 0 10 10"><circle cx="5" cy="5" r="4" fill="none" stroke="#8cff0a"/><path d="M1 5 H9 M5 1 Q2.5 5 5 9 M5 1 Q7.5 5 5 9" fill="none" stroke="#8cff0a"/></svg>www.haldenconsulting.com</div>
  </div>
  <div class="greeting">With compliments</div>
  <div class="bar"></div>
</section>

</body>
</html>
```